BRISK Signal Partners Business Card Rebrand

Hello Designers! We are looking for help designing our new business card to go in conjunction with our company rebrand. Unfortunately, we have an event mid June that requires we get these printed ASAP (before our new website is launched.) We have a mostly complete Brand Book which I have uploaded to this request for your reference to company information, style, fonts. I've also enclosed our logo file in .eps & .jpg. Attached is a sample business card my boss liked but said was "too simple." I made it in Canva and do not profess to be a designer. NOT FOR DESIGN REFERENCE, ONLY FOR CONTEXT Here is what our old website looks like: https://brisksignalpartners-demo.net/.
Sick
Sick
Sick

```html
<!DOCTYPE html>
<html lang="en">
<head>
<meta charset="utf-8">
<title>BRISK Signal Partners – Business Card</title>
<link href="https://fonts.googleapis.com/css2?family=Montserrat:wght@400;500;700&display=swap" rel="stylesheet">
<style>
  :root {
    --bg: #2b2b30;
    --card-black: #0d0d0f;
    --card-white: #ffffff;
    --brand-blue: #4cb3e8;
    --ink: #111111;
    --ink-soft: #2a2a2a;
    --pattern-dark: #1a1a1d;
    --pattern-light: #d8d8d8;
  }
  * { box-sizing: border-box; margin: 0; padding: 0; }
  html, body { width: 1200px; height: 900px; overflow: hidden; }
  body {
    background: var(--bg);
    font-family: "Montserrat", sans-serif;
    position: relative;
  }
  .card {
    position: absolute;
    left: 250px;
    width: 700px;
    height: 400px;
    border-radius: 22px;
    overflow: hidden;
  }
  /* Back side */
  .card--back { top: 40px; background: var(--card-black); }
  .card-back__pattern {
    position: absolute; inset: 0;
    background: radial-gradient(ellipse at 0% 80%, var(--pattern-light) 0%, #5a5a5e 22%, var(--pattern-dark) 50%, var(--card-black) 100%);
  }
  .card-back__brand {
    position: absolute; right: 70px; top: 150px;
    display: flex; align-items: center; gap: 16px;
  }
  .brand-dot { width: 64px; height: 64px; border-radius: 50%; background: var(--brand-blue); flex: none; }
  .brand-name { font-weight: 700; font-size: 30px; line-height: 1.05; letter-spacing: 0.5px; }
  .card-back__brand .brand-name { color: #ffffff; }

  /* Front side */
  .card--front { top: 460px; background: var(--card-white); }
  .card-front__brand {
    position: absolute; left: 60px; top: 150px;
    display: flex; align-items: center; gap: 16px;
  }
  .card-front__brand .brand-name { color: var(--ink); }
  .card-front__divider {
    position: absolute; left: 360px; top: 60px;
    width: 2px; height: 210px; background: var(--brand-blue);
  }
  .contact {
    position: absolute; left: 385px; top: 58px;
    color: var(--ink-soft);
  }
  .contact__name { color: var(--brand-blue); font-weight: 700; font-size: 25px; }
  .contact__title { font-size: 13px; font-weight: 500; letter-spacing: 0.5px; margin-top: 4px; }
  .contact__location { font-size: 13px; margin-top: 14px; }
  .contact__list { list-style: none; margin-top: 14px; }
  .contact__item { display: flex; align-items: center; gap: 10px; font-size: 13px; margin-bottom: 9px; }
  .contact__icon { width: 14px; height: 14px; flex: none; }
  .card-front__address {
    position: absolute; left: 385px; bottom: 48px;
    font-size: 13px; color: var(--ink-soft);
  }
</style>
</head>
<body>
  <section class="card card--back" aria-label="Card back">
    <div class="card-back__pattern" role="img" aria-label="Repeating brand symbol pattern in glossy black with silver highlights"></div>
    <div class="card-back__brand">
      <span class="brand-dot"></span>
      <span class="brand-name">BRISK Signal<br>Partners</span>
    </div>
  </section>

  <section class="card card--front" aria-label="Card front">
    <div class="card-front__brand">
      <span class="brand-dot"></span>
      <span class="brand-name">BRISK Signal<br>Partners</span>
    </div>
    <div class="card-front__divider"></div>
    <div class="contact">
      <p class="contact__name">Marcus Delaney-Holt</p>
      <p class="contact__title">MANAGING PARTNER</p>
      <p class="contact__location">Riverton, GA based (Central Time)</p>
      <ul class="contact__list">
        <li class="contact__item">
          <svg class="contact__icon" viewBox="0 0 16 16"><path fill="#4cb3e8" d="M3 1h3l1.5 4-2 1.2a9 9 0 0 0 4.3 4.3L11 8.5l4 1.5v3a2 2 0 0 1-2 2C6.4 15 1 9.6 1 3a2 2 0 0 1 2-2z"/></svg>
          +945-555-0142
        </li>
        <li class="contact__item">
          <svg class="contact__icon" viewBox="0 0 16 16"><rect x="1" y="3" width="14" height="10" rx="1" fill="#4cb3e8"/><path d="M1.5 3.5 8 9l6.5-5.5" fill="none" stroke="#fff" stroke-width="1.3"/></svg>
          marcus@brisksignalpartners-demo.net
        </li>
        <li class="contact__item">
          <svg class="contact__icon" viewBox="0 0 16 16"><circle cx="8" cy="8" r="7" fill="#4cb3e8"/><path d="M1 8h14M8 1c-3 3.5-3 10.5 0 14M8 1c3 3.5 3 10.5 0 14" fill="none" stroke="#fff" stroke-width="1"/></svg>
          www.brisksignalpartners-demo.net
        </li>
      </ul>
    </div>
    <p class="card-front__address">PO Box 40117, Springdale, TN 37000</p>
  </section>
</body>
</html>
```